Re-Brand of TindelMox along with a new website design

TindelMox Ltd are a software & database development company using technologies such as PHP, C#, HTML, JQuery, Flex, AS3, MySQL, Oracle, MSSQL. We like to target all types of business from small to large.

We are great at coding but rubbish at design so thats where we need your help!

We want a complete re-brand of TindelMox including logo, website design, and business cards.

We would like a design that is clean but other than that, please feel free to be creative.

****Logo****
We are looking for a logo that appears professional but with a splash of colour that indicates a creative side. Please see below some logos that we like the look of:

We like this one because it has a nice simple and clear font for the name of the company but also an icon which is colourful and stands out. http://markvault.example/2013/03/brivelo/

We like this one because it is very clean, simple and again very clear. http://markvault.example/2013/03/quantorels/

http://markvault.example/2013/03/tide-lamp/
http://markvault.example/2013/02/velmorin/
http://markvault.example/2013/01/art-gallery-tarnwick/

As you will see from all of these examples, the font is very clear but there is always a graphic representing the company too. This is what we like.

****Website****
These are some of the examples of websites we like:
https://www.zestrune.example/
https://www.chatterlane.example/home
http://www.haldenimagery.example/
http://www.vistor.example/
http://quillbay.example/
https://www.usebriefnest.example/personal-intros
http://www.marmotpanel.example/

The current site can be found at tindelmox.example.uk

Reason: We have extended the deadline of the project by 5 days as I realise the original deadline was very tight.

Software

Requirements
Must have
• Website must have the following pages
Home
Services
Projects
About Us
Contact Us

```html
<!DOCTYPE html>
<html lang="en">
<head>
<meta charset="utf-8">
<title>TindelMox – IT Services</title>
<link rel="stylesheet" href="https://fonts.googleapis.com/css2?family=Lato:wght@300;400&family=Raleway:wght@200;300&display=swap">
<style>
  :root {
    --ink: #0b0b0d;
    --hero-deep: #0a1a3a;
    --hero-mid: #1f4f9a;
    --hero-glow: #8fc4f2;
    --accent: #2a8fd6;
    --text-grey: #6d6d70;
    --band-grey: #d9d9db;
    --footer-bg: #0d0d0f;
    --footer-text: #bdbdc0;
    --showcase-core: #dcebf8;
    --showcase-edge: #9cc3e8;
    --white: #ffffff;
  }
  * { box-sizing: border-box; margin: 0; padding: 0; }
  html, body { width: 818px; height: 1200px; overflow: hidden; background: var(--white); }
  body { font-family: "Lato", Arial, sans-serif; color: var(--text-grey); position: relative; }

  .site-header { position: absolute; top: 0; left: 0; width: 818px; height: 82px; background: var(--ink); z-index: 2; }
  .brand-tab {
    position: absolute; left: 50%; top: 0; transform: translateX(-50%);
    width: 190px; height: 38px; background: var(--white);
    display: flex; align-items: center; justify-content: center;
    border-radius: 0 0 6px 6px;
  }
  .brand-name { font-weight: 400; font-size: 24px; color: var(--ink); letter-spacing: 1px; }
  .main-nav { position: absolute; top: 52px; left: 0; width: 818px; display: flex; justify-content: center; gap: 34px; }
  .main-nav a { color: var(--white); text-decoration: none; font-size: 15px; font-weight: 300; }

  .hero {
    position: absolute; top: 82px; left: 0; width: 818px; height: 258px;
    background: radial-gradient(ellipse at 70% 60%, var(--hero-glow) 0%, var(--hero-mid) 35%, var(--hero-deep) 80%);
  }
  .hero-title {
    position: absolute; top: 88px; width: 100%; text-align: center;
    font-family: "Raleway", Arial, sans-serif; font-weight: 200; font-size: 62px; color: var(--white);
  }

  .intro { position: absolute; top: 352px; left: 0; width: 818px; text-align: center; z-index: 1; }
  .intro-lead { font-family: "Raleway", Arial, sans-serif; font-weight: 300; font-size: 24px; line-height: 32px; }
  .intro-service { font-family: "Raleway", Arial, sans-serif; font-weight: 300; font-size: 34px; line-height: 38px; color: var(--accent); }
  .intro-pitch { font-family: "Raleway", Arial, sans-serif; font-weight: 300; font-size: 23px; line-height: 30px; }

  .showcase {
    position: absolute; top: 520px; left: 0; width: 818px; height: 350px;
    background: radial-gradient(ellipse 300px 190px at 50% 55%, var(--showcase-edge) 0%, var(--showcase-core) 45%, var(--white) 100%);
  }

  .divider { position: absolute; top: 870px; left: 0; width: 818px; height: 26px; background: var(--ink); z-index: 2; }
  .divider svg { position: absolute; left: 374px; top: 25px; }

  .about { position: absolute; top: 896px; left: 0; width: 818px; height: 180px; background: var(--band-grey); text-align: center; padding-top: 28px; }
  .about p { font-size: 13px; font-weight: 300; line-height: 17px; margin-bottom: 12px; }

  .site-footer { position: absolute; top: 1076px; left: 0; width: 818px; height: 124px; background: var(--footer-bg); color: var(--footer-text); font-size: 10.5px; line-height: 13px; }
  .footer-nav { position: absolute; left: 122px; top: 10px; list-style: none; }
  .footer-nav a { color: var(--footer-text); text-decoration: none; }
  .footer-contact { position: absolute; left: 258px; top: 10px; }
  .footer-contact dl { display: grid; grid-template-columns: 70px auto; margin-top: 6px; }
  .footer-social { position: absolute; left: 598px; top: 12px; text-align: center; width: 130px; }
  .social-links { display: flex; justify-content: center; gap: 10px; color: var(--white); font-size: 10.5px; margin-bottom: 8px; }
</style>
</head>
<body>
  <header class="site-header">
    <div class="brand-tab"><span class="brand-name">TindelMox</span></div>
    <nav class="main-nav">
      <a href="#">home</a><a href="#">services</a><a href="#">projects</a><a href="#">about us</a><a href="#">contact us</a>
    </nav>
  </header>

  <section class="hero" role="img" aria-label="Blue technology photograph of a hand reaching into a glowing circuit network">
    <h1 class="hero-title">welcome to TindelMox</h1>
  </section>

  <div class="showcase" role="img" aria-label="Illustration of a laptop inside a glowing glass sphere"></div>

  <section class="intro">
    <p class="intro-lead">If you are looking for</p>
    <p class="intro-service">web</p>
    <p class="intro-service">software</p>
    <p class="intro-service">IT services</p>
    <p class="intro-pitch">that really deliver but you don't want to pay over the odds</p>
    <p class="intro-pitch">then TindelMox is the right team for you</p>
  </section>

  <div class="divider">
    <svg width="70" height="20" viewBox="0 0 70 20"><polygon points="0,0 70,0 35,20" fill="var(--ink)"/></svg>
  </div>

  <section class="about">
    <p>Based in Ashbury our clients are both local, national, both large and small.<br>You may be a start-up business in need of a 'get me up and running quickly' website,<br>or a multi-million pound brand looking for an all singing, all dancing bespoke app.</p>
    <p>Maybe you are experiencing the pains and pleasures of growing your business<br>and its time to improve your branding<br>and to trade in your current home spun website for something more professional.</p>
    <p>Let's chat today about where we can take your business.</p>
  </section>

  <footer class="site-footer">
    <ul class="footer-nav">
      <li><a href="#">home</a></li><li><a href="#">services</a></li><li><a href="#">projects</a></li><li><a href="#">about us</a></li><li><a href="#">contact us</a></li>
    </ul>
    <div class="footer-contact">
      <div>TindelMox</div>
      <dl>
        <dt>Telephone</dt><dd>01632 480 215</dd>
        <dt>Email</dt><dd>contact@tindelmox.example.uk</dd>
        <dt>Address</dt><dd>15 Marrowdale Road<br>Ashbury<br>Northshire<br>AB1 2CD</dd>
      </dl>
    </div>
    <div class="footer-social">
      <div class="social-links"><span>Linkora</span><span>Chirpel</span><span>Plusvo</span></div>
      <div>© Copyright 2013 TindelMox<br>All Rights Reserved<br>Terms of Use</div>
    </div>
  </footer>
</body>
</html>
```